Freelance film producer/editor wants you to brisk vanta!

'Brisk Vanta' is my production business based in Melbourne, though I do a fair bit of work overseas. I'm a one woman show most of the time but enlist other crew members for larger projects. I manage productions from start to finish including producing, filming, editing, distribution, photography and animation.

My current tag line and details are as follows:

Greta Hollensby
Producer. Editor. Thinker.
[M] +61 417 562 093
[E] gh[at]briskvanta.com.au
www.briskvanta.com.au

I have a fairly wicked sense of humour and love a good pun, so feel free to work this into your design!

The final designs should demonstrate the areas I work in but not limited to. I'd rather not use old and typical "film" looking elements such as a clapper or negative reel. Having said that, the logo itself (attached) is quite typical because the first 'o' is a closed aperture and the second is a wide aperture. Happy for the logo to be pulled apart for the business card to be more interesting.

The majority of projects I work on are quite different and in some cases a bit crazy. Lots of travel involved. The main difference between me and other producers is that I don't say I work in 'film', even though i do. I want the card to leave me open to new roles and projects as opposed to squashing myself into one particular category.

I'm open to colour but prefer a simple design that isn't too hectic.

I have also attached an example I did like that was printed on plastic but then I realised so many other people had ripped it off....

I'm open to paper board or plastic (transparent) designs etc. One sided or two sided.

Thanks for sharing your ideas with me and please, go as nuts as you want to with this! :)

Target Market(s)

My clients range from non profits in health and educational institutions to record labels and well known artists. The business attracts corporates as well though the majority of my business is achieved through referral and word of mouth so most people will soon realise that my personality and work are very much intertwined and the reason they hire me for a job.

Industry/Entity Type

Business

Font styles to use
Other font styles liked:
• Eurostile or similar

Requirements
Must have
• I have a very open mind when it comes to design. I do like the existing tag line but if you can come up with something better I'm all ears! (and eyes)

Nice to have
• Back of the business card can be graphics, there can be transparent elements or holes, embossing options...
Should not have
• Besides my name, nothing should scream "I am woman!" because in my industry that's not a selling point.

The colour pink is a definite no.

```html
<!DOCTYPE html>
<html lang="en">
<head>
<meta charset="utf-8">
<title>Brisk Vanta – Business Card</title>
<link rel="stylesheet" href="https://fonts.googleapis.com/css2?family=Open+Sans:wght@300;600;700&display=swap">
<style>
  :root{
    --canvas:#d9dcdb;
    --band:#222224;
    --white:#ffffff;
    --mist-top:#f4f5f5;
    --mist-bottom:#c9cbcb;
    --sky-light:#eaf6fb;
    --sky-deep:#4fc3ec;
    --red:#e8202a;
    --orange:#f47a20;
    --yellow:#f2e21c;
    --green:#5cbf2a;
    --cyan:#2aa9e0;
    --blue:#2f6fd6;
    --violet:#6a3fb8;
  }
  *{margin:0;padding:0;box-sizing:border-box}
  html,body{width:1200px;height:1000px;overflow:hidden;background:var(--canvas)}
  .canvas{position:relative;width:1200px;height:1000px}
  .card{position:absolute;left:220px;width:760px;height:464px;overflow:hidden;border-radius:4px;box-shadow:0 6px 18px rgba(0,0,0,.18)}
  .card--front{top:24px}
  .card--back{top:512px}
  .card__art{position:absolute;inset:0;width:760px;height:464px;display:block}
  .band{fill:var(--band)}
  .spectrum{fill:url(#spectrum)}
  .spectrum--back{fill:url(#spectrum-back)}
  .wordmark{position:absolute;left:420px;top:230px;transform:rotate(15deg);transform-origin:left top;
    font-family:'Open Sans',sans-serif;font-weight:300;font-size:64px;letter-spacing:1px;color:var(--white);white-space:nowrap}
  .contact{position:absolute;right:30px;top:34px;text-align:right;font-family:'Open Sans',sans-serif;font-style:normal;color:var(--white);line-height:1.55}
  .contact__name{font-weight:700;font-size:22px;letter-spacing:1px}
  .contact__line{font-weight:600;font-size:17px;letter-spacing:.5px}
  .tagline{position:absolute;left:30px;bottom:26px;font-family:'Open Sans',sans-serif;font-weight:700;font-size:20px;line-height:1.4;color:var(--white);letter-spacing:1px}
</style>
</head>
<body>
<main class="canvas">

  <section class="card card--front" aria-label="Card front">
    <svg class="card__art" viewBox="0 0 760 464">
      <defs>
        <linearGradient id="mist" x1="0" y1="0" x2="0" y2="1">
          <stop offset="0" stop-color="var(--mist-top)"/>
          <stop offset="1" stop-color="var(--mist-bottom)"/>
        </linearGradient>
        <linearGradient id="spectrum" x1="0" y1="0" x2="1" y2="0">
          <stop offset="0" stop-color="var(--violet)"/>
          <stop offset=".17" stop-color="var(--blue)"/>
          <stop offset=".34" stop-color="var(--cyan)"/>
          <stop offset=".5" stop-color="var(--green)"/>
          <stop offset=".66" stop-color="var(--yellow)"/>
          <stop offset=".83" stop-color="var(--orange)"/>
          <stop offset="1" stop-color="var(--red)"/>
        </linearGradient>
      </defs>
      <rect width="760" height="464" fill="url(#mist)"/>
      <path class="spectrum" role="img" aria-label="Rainbow equaliser bars rising above the band"
            d="M200,200 L200,100 Q480,130 760,230 L760,330 Z"/>
      <path class="spectrum" role="img" aria-label="Rainbow equaliser bars hanging below the band"
            d="M0,240 Q300,320 600,464 L430,464 Q210,380 0,330 Z"/>
      <path class="band" d="M0,110 Q400,190 760,300 L760,464 L560,464 Q300,330 0,250 Z"/>
    </svg>
    <p class="wordmark">brisk vanta</p>
  </section>

  <section class="card card--back" aria-label="Card back">
    <svg class="card__art" viewBox="0 0 760 464">
      <defs>
        <linearGradient id="sky" x1="0" y1="1" x2="1" y2="0">
          <stop offset="0" stop-color="var(--sky-light)"/>
          <stop offset="1" stop-color="var(--sky-deep)"/>
        </linearGradient>
        <linearGradient id="spectrum-back" x1="0" y1="0" x2="1" y2="0">
          <stop offset="0" stop-color="var(--violet)"/>
          <stop offset=".2" stop-color="var(--red)"/>
          <stop offset=".4" stop-color="var(--yellow)"/>
          <stop offset=".6" stop-color="var(--green)"/>
          <stop offset=".8" stop-color="var(--cyan)"/>
          <stop offset="1" stop-color="var(--blue)"/>
        </linearGradient>
      </defs>
      <rect width="760" height="464" fill="url(#sky)"/>
      <path class="spectrum--back" role="img" aria-label="Rainbow equaliser bars rising along the lower band"
            d="M0,262 Q230,300 420,464 L300,464 Q150,370 0,330 Z"/>
      <path class="band" d="M260,0 H760 V260 Q520,210 260,0 Z"/>
      <path class="band" d="M0,300 Q220,360 420,464 H0 Z"/>
    </svg>
    <address class="contact">
      <p class="contact__name">Greta Hollensby</p>
      <p class="contact__line">[M] +61 417 562 093</p>
      <p class="contact__line">[E] gh[at]briskvanta.com.au</p>
      <p class="contact__line">www.briskvanta.com.au</p>
    </address>
    <p class="tagline">Producer.<br>Editor.<br>Thinker.</p>
  </section>

</main>
</body>
</html>
```